Gestaltung einer Webseite für Eventfotografie
quirlmoos hat hervorragende Arbeit geleistet. Das Design ist 1A, sowie die weitere Projektabwicklung, völlig problemlos, sehr freundlich, entgegenkommend und kompetent. Ich kann quirlmoos jederzeit mit 5 Sternen als Designer weiterempfehlen! gernold
Zielgruppe
Eventagenturen, Entscheider in Marketing- bzw. Eventabteilungen von mittelständischen oder großen Firmen sowie Bankettabteilungen von Hotels.
Aufgabenstellung
Neuerstellung Webseitenlayout und programmtechnische Umsetzung einer Webseite.
Die Webseite soll "Das Glanzstück"heissen. Die Wörter "Das Glanzstück" wären grafisch dementsprechend auch zu gestalten.
Die Webseite dient als Schaufenster zur Generierung von Anfragen / Aufträgen die Eventfotografie betreffend. Da der erste Eindruck entscheidend ist, stelle ich mir beim Aufruf der Webseite vor, dass prominent 3-5 Fotos erscheinen. Die Animation der Fotos soll so gestaltet sein, als wenn man Papierabzüge auf einen Tisch legt (Mein Haus, Mein Pferd, mein Boot...)
Darüber hinaus sollen weitere weniger auffällige Eventfotos erscheinen.
Es sollen eine Homepage, eine Kontaktseite, eine Fotogalerieseite, eine Referenzseite (mit Kundennamen und Fotos) und evtl. ein Onlinekalender integriert sein, auf dem der Benutzer das Eventdatum anklicken und seine Anfrage platzieren kann. Impressum ist obligatorisch.
Alle Bereiche sollen übersichtlich und klar gestaltet sein, so dass sich der User schnell orientieren kann.
Auf jeder Unterseite soll ein ca. 5DM-Stück grosser auffälliger "Termin-Anfrage"-Button platziert sein.

```html
<!DOCTYPE html>
<html lang="de">
<head>
<meta charset="utf-8">
<title>Das Glanzstück – Eventfotografie</title>
<link href="https://fonts.googleapis.com/css2?family=Arimo:wght@400;700&family=Caveat:wght@600&display=swap" rel="stylesheet">
<style>
:root{
  --pink:#e5135f;
  --grey:#8c8c8c;
  --line:#8a8a8a;
  --text:#111;
  --white:#fff;
}
*{margin:0;padding:0;box-sizing:border-box}
html,body{width:1200px;height:1172px;overflow:hidden}
body{
  position:relative;
  font-family:"Arimo",Arial,sans-serif;
  background:radial-gradient(ellipse 75% 72% at 50% 50%,#fff 68%,#ededed 84%,#a9a9a9 100%);
}
.brand{position:absolute;left:76px;top:56px;display:flex;align-items:center;gap:12px}
.brand-mark{width:14px;height:14px;background:var(--pink)}
.brand-name{font-size:36px;font-weight:700;color:var(--pink);text-transform:uppercase;letter-spacing:1px;line-height:1}
.main-nav{position:absolute;left:509px;top:58px;display:flex;gap:2px}
.main-nav a{display:block;width:127px;border-top:7px solid var(--line);padding-top:14px;text-align:right;font-size:15px;font-weight:700;color:var(--grey);text-decoration:none}
.main-nav a.active{border-color:var(--pink);color:var(--pink)}
.appointment{position:absolute;left:1040px;top:0;width:160px;height:160px}
.appointment-hint{position:absolute;left:1050px;top:126px;font-family:"Caveat",cursive;font-size:15px;color:var(--white);line-height:15px;text-align:center;text-shadow:0 0 3px #333;transform:rotate(5deg)}
.slider-dots{position:absolute;left:540px;top:152px;display:flex;align-items:center;gap:24px}
.slider-dots span{width:11px;height:11px;border-radius:50%;background:#111}
.slider-dots span.active{width:24px;height:24px;background:var(--pink)}
.slide{position:absolute}
.slide-side{top:311px;height:295px;width:176px}
.slide-left{left:0;background:linear-gradient(90deg,#15181d 0%,#3d4550 25%,#9aa0a6 45%,#c9c9c9 62%,#2a2e35 85%,#15181d 100%)}
.slide-right{left:1024px;background:linear-gradient(180deg,#3a3838 0%,#9c9a97 35%,#6a625c 60%,#2c2522 80%,#4a3f38 100%)}
.slide-main{left:176px;top:188px;width:848px;height:476px;z-index:2;
  background:
    linear-gradient(90deg,rgba(255,255,255,.10) 0%,rgba(0,0,0,0) 30%,rgba(255,255,255,.08) 60%,rgba(0,0,0,.15) 100%),
    linear-gradient(180deg,#0f0f0f 0%,#1c1c1c 10%,#5e5c5a 30%,#4b4947 45%,#1e1e1e 55%,#cfcfcf 64%,#ececec 72%,#bdbdbd 82%,#2b2a2a 92%,#1a1a1a 100%);}
.slide-shadow{position:absolute;left:180px;top:660px;width:840px;height:64px;border-radius:50%;background:radial-gradient(ellipse at center,rgba(0,0,0,.95) 30%,rgba(0,0,0,0) 70%)}
.slide-arrow{position:absolute;top:619px;z-index:3;width:53px;height:53px}
.slide-arrow.prev{left:169px}
.slide-arrow.next{left:979px}
.features{position:absolute;left:59px;top:770px;width:1083px;height:183px;background:var(--white);box-shadow:0 14px 22px rgba(0,0,0,.12);display:flex;padding:30px 0 0 35px}
.feature{width:349px;padding-right:40px}
.feature h2{font-size:17px;font-weight:700;color:var(--pink);margin-bottom:30px}
.feature p{font-size:13px;line-height:14px;color:var(--text)}
.footer-nav{position:absolute;left:766px;top:1104px;display:flex;gap:2px}
.footer-nav a{display:block;width:127px;border-bottom:7px solid var(--line);padding-bottom:10px;text-align:right;font-size:14px;font-weight:700;color:var(--grey);text-decoration:none}
.footer-nav a:first-child{padding-right:22px}
</style>
</head>
<body>
<header>
  <div class="brand"><span class="brand-name">Das Glanzstück</span><span class="brand-mark"></span></div>
  <nav class="main-nav">
    <a class="active" href="#">startseite</a>
    <a href="#">über uns</a>
    <a href="#">galerie</a>
    <a href="#">portfolio</a>
  </nav>
  <svg class="appointment" viewBox="0 0 160 160" aria-label="Termin vereinbaren">
    <polygon points="20,0 82,0 160,78 160,140" fill="#e5135f"/>
    <text x="110" y="40" transform="rotate(45 110 40)" fill="#fff" font-family="Arimo,Arial,sans-serif" font-size="15" text-anchor="middle">TERMIN</text>
    <text x="98" y="55" transform="rotate(45 98 55)" fill="#fff" font-family="Arimo,Arial,sans-serif" font-size="15" text-anchor="middle">vereinbaren</text>
    <path d="M42 120 C44 104 48 94 58 84" stroke="#fff" stroke-width="3" fill="none" stroke-linecap="round"/>
    <path d="M50 84 L59 82 L59 92" stroke="#fff" stroke-width="3" fill="none" stroke-linecap="round" stroke-linejoin="round"/>
  </svg>
  <div class="appointment-hint">klicken Sie hier<br>für einen Termin</div>
</header>

<main>
  <div class="slider-dots"><span class="active"></span><span></span><span></span><span></span></div>
  <div class="slide slide-side slide-left" role="img" aria-label="Eventfoto: Ausstellungswand mit Modefotografie"></div>
  <div class="slide slide-side slide-right" role="img" aria-label="Eventfoto: Gäste vor einer Fahrzeugpräsentation"></div>
  <div class="slide-shadow"></div>
  <div class="slide slide-main" role="img" aria-label="Eventfoto: Gäste auf weißen Sofas in einer Galerie mit gerahmten Porträts"></div>
  <svg class="slide-arrow prev" viewBox="0 0 53 53" aria-label="zurück">
    <polygon points="0,0 0,53 53,53" fill="#e5135f"/>
    <path d="M22 31 L10 31 M15 26 L10 31 L15 36" stroke="#fff" stroke-width="4" fill="none"/>
  </svg>
  <svg class="slide-arrow next" viewBox="0 0 53 53" aria-label="weiter">
    <polygon points="53,0 53,53 0,53" fill="#e5135f"/>
    <path d="M31 31 L43 31 M38 26 L43 31 L38 36" stroke="#fff" stroke-width="4" fill="none"/>
  </svg>

  <section class="features">
    <article class="feature">
      <h2>PROFESSIONELLE FOTOGRAFIE</h2>
      <p>Lorem ipsum dolor sit amet, consetetur sadipscing elitr, sed diam nonumy eirmod tempor invidunt ut labore et dolore magna aliquyam erat, sed diam voluptua.<br>At vero eos et accusam et justo duo dolores et ea rebum.</p>
    </article>
    <article class="feature">
      <h2>QUALITATIVE BILDBEARBEITUNG</h2>
      <p>Lorem ipsum dolor sit amet, consetetur sadipscing elitr, sed diam nonumy eirmod tempor invidunt ut labore et dolore magna aliquyam erat, sed diam voluptua. At vero eos et accusam et justo duo dolores et ea rebum.</p>
    </article>
    <article class="feature">
      <h2>TOP PREIS-LEISTUNG</h2>
      <p>Lorem ipsum dolor sit amet, consetetur sadipscing elitr.<br>Sed diam nonumy eirmod tempor invidunt ut labore et dolore magna aliquyam erat, sed diam voluptua. At vero eos et accusam et justo duo dolores et ea rebum</p>
    </article>
  </section>
</main>

<footer>
  <nav class="footer-nav">
    <a href="#">impressum</a>
    <a href="#">kontakt</a>
  </nav>
</footer>
</body>
</html>
```